Corporate flyer highlighting service offering for PR agency

A corporate flyer is needed for a new service offering that we are doing. The product name is HarborLeap it is a marketing and communications services offering for companies who are getting ready to sell their business. If we are really happy with the designer's work, there will be a great deal more projects. I am looking for a clean design with a few pops of color from my site. https://quillmarsh.partners. I am looking for a good design with data in sections. I am looking for a clean design that feels high-end but not cluttered. Please do not use images of people. Please see the following examples of types of designs I like.
https://www.tackboard.example/pin/839201746530918264/
https://www.tackboard.example/pin/402918375561029847/
https://assets.stockvale.example/corporate-flyer-template-KRTPMB
https://designbrook.example/item/corporate-flyer-template/81046395?s_rank=8
https://assets.stockvale.example/corporate-business-flyer-template-93PX7D

I had to place the project on hold as I choose the wrong type of project and did not get many designs as a result. I am reposting this with an updated brief.

Target Market(s)

Business sellers and brokers

Industry/Entity Type

Marketing for business sellers

Font styles to use
Sans Serif

Requirements
Must have
• Good quality design with content in sections. Clean and high end feeling is a must.
Should not have
• A lot of images of people.

```html
<!DOCTYPE html>
<html lang="en">
<head>
<meta charset="utf-8">
<title>HarborLeap Flyer – Quillmarsh Partners</title>
<link rel="stylesheet" href="https://fonts.googleapis.com/css2?family=Red+Hat+Display:ital,wght@0,400;0,500;0,600;0,700;1,700&family=Red+Hat+Text:ital,wght@0,400;0,500;1,500&display=swap">
<style>
:root{
  --blue:#1f8bd0;
  --blue-dark:#1b6fb0;
  --sky:#c3e5f8;
  --orange:#f7941d;
  --orange-deep:#f15a24;
  --ink:#333740;
  --backdrop:#b3b3b3;
  --paper:#ffffff;
}
*{margin:0;padding:0;box-sizing:border-box}
html,body{width:1200px;height:1200px;overflow:hidden;background:var(--backdrop)}
body{font-family:"Red Hat Text",Arial,sans-serif;color:var(--ink)}
.board{position:absolute;left:0;top:0;width:1932px;height:1932px;transform:scale(.62112);transform-origin:0 0}
.page{position:absolute;width:634px;height:895px;background:var(--paper);overflow:hidden}
.p1{left:308px;top:55px}.p2{left:961px;top:55px}.p3{left:308px;top:975px}.p4{left:961px;top:975px}
.a{position:absolute}
.body{font-size:12px;line-height:15.5px}
.disp{font-family:"Red Hat Display",Arial,sans-serif}
.strip{position:absolute;left:0;bottom:0;width:100%;height:13px;background:var(--blue)}
.tick{position:absolute;left:0;top:2px;width:10px;height:10px;border-radius:50%;background:var(--orange)}
.tick::after{content:"";position:absolute;left:3.3px;top:1.8px;width:2.6px;height:4.6px;border:solid #fff;border-width:0 1.5px 1.5px 0;transform:rotate(45deg)}
.tick.light{background:#fff;width:13px;height:13px}
.tick.light::after{border-color:var(--blue);left:4.3px;top:2.3px;width:3.2px;height:6px}
.list{list-style:none}
.list li{position:relative;padding-left:23px}
.blue-b{color:var(--blue);font-weight:700;font-family:"Red Hat Display",Arial,sans-serif}
.orange-b{color:var(--orange);font-weight:700;font-family:"Red Hat Display",Arial,sans-serif}

/* page 1 */
.brand{left:50px;top:95px;width:240px;display:flex;align-items:center;gap:10px}
.brand-mark{width:18px;height:18px;background:var(--blue)}
.brand-name{font-family:"Red Hat Display",sans-serif;font-weight:700;font-size:22px;color:#2b2d33;letter-spacing:.5px;line-height:1}
.hero-svg{left:0;top:0}
.hero-title{left:50px;top:202px;width:285px;color:#fff;font-family:"Red Hat Display",sans-serif;font-weight:500;font-size:21.5px;line-height:26.5px}
.lead-bar{left:71px;top:376px;width:4px;height:128px;background:var(--orange)}
.lead{left:103px;top:374px;width:470px}
.lead p+p{margin-top:16px}
.callout{left:0;top:522px}
.callout-text{left:90px;top:542px;width:460px;text-align:center;font-size:11.5px;line-height:14.5px}
.callout-text em{font-weight:500;display:block;margin-bottom:8px}
.support{left:50px;top:660px;width:360px;font-size:12.5px;line-height:20.4px}
.stages{left:408px;top:661px;font-size:12.5px;line-height:17px;font-weight:700;font-family:"Red Hat Display",sans-serif}
.stages li{padding-left:19px}
.band-foot{left:0;top:782px;width:634px;height:113px;background:var(--blue);color:#fff;font-family:"Red Hat Display",sans-serif;font-weight:700;font-size:12px;line-height:16px;text-align:center;padding:19px 60px 0}

/* page 2 */
.team{left:55px;top:38px;width:530px}
.band-blue{left:0;top:145px;width:634px;height:117px;background:var(--blue);color:#fff;font-family:"Red Hat Display",sans-serif;font-weight:700;font-size:13.5px;line-height:17.5px;text-align:center;padding:15px 55px 0}
.help-title{left:0;top:270px;width:634px;text-align:center;font-size:16px}
.pillar{top:298px;width:130px;text-align:center}
.pillar .ring{width:70px;height:70px;border:2px solid var(--orange);border-radius:50%;margin:0 auto 10px;position:relative}
.pillar .ring::after{content:"";position:absolute;left:24px;top:24px;width:18px;height:18px;background:var(--blue)}
.pillar p{font-family:"Red Hat Display",sans-serif;font-weight:600;font-size:12px;line-height:14.5px;color:#2b2d33}
.rule{left:55px;top:466px;width:526px;height:2px;background:var(--blue)}
.intro2{left:55px;top:483px;width:520px}
.sec-title{font-size:16px}
.brand-items{left:55px;top:624px;width:510px}
.brand-items li{margin-bottom:14px}
.brand-items li .orange-b{font-size:12px;display:block}

/* page 3 */
.stat-box{left:50px;width:535px;height:109px;color:#fff;font-family:"Red Hat Display",sans-serif;font-weight:500;font-size:16px;line-height:21px;text-align:center;padding:21px 20px 0}
.stat-notch{position:absolute;left:450px;bottom:-22px;width:0;height:0;border-left:25px solid transparent;border-right:25px solid transparent}
.mk-title{left:50px;top:330px;font-size:16px}
.mk-left{left:50px;top:372px;width:240px;font-size:12px;line-height:16.2px}
.mk-list{left:50px;top:530px;width:240px}
.mk-list li{margin-bottom:16.5px;font-size:12.5px;line-height:16.2px}
.mk-right{left:320px;top:372px;width:265px}
.mk-right .orange-b{font-size:12px;line-height:14px}
.mk-right .body{margin-top:10px;font-size:12px;line-height:16.2px}
.msg-list{left:330px;top:602px;width:260px}
.msg-list li{margin-bottom:16px;font-size:12.5px;line-height:16.2px}

/* page 4 */
.media-title{left:53px;top:38px;font-size:16px}
.media-body{left:53px;top:74px;width:500px}
.media-list{left:55px;top:162px;width:490px}
.media-list li{margin-bottom:13px;font-size:12px;line-height:15px;padding-left:25px}
.sky-band{left:0;top:308px;width:634px;height:190px;background:var(--sky)}
.deep-band{left:0;top:498px;width:634px;height:387px;background:var(--blue)}
.orange-strip{left:0;top:883px;width:634px;height:12px;background:var(--orange)}
.wh-title{left:53px;top:328px;font-size:17px;color:var(--blue-dark)}
.wh-body{left:60px;top:366px;width:495px;font-size:11.5px;line-height:14px}
.quote-text{left:70px;top:470px;width:500px;text-align:center;color:#fff;font-family:"Red Hat Display",sans-serif;font-weight:700;font-style:italic;font-size:15px;line-height:21px}
.after{left:60px;top:572px;width:480px;color:#fff;font-size:11.5px;line-height:16px}
.product{left:60px;width:500px;color:#fff}
.product h4{font-family:"Red Hat Display",sans-serif;font-weight:600;font-size:14px;padding-left:38px;position:relative}
.product h4 .tick{top:1px}
.product p{margin-top:20px;padding-left:38px;font-size:11.5px;line-height:14.5px}
</style>
</head>
<body>
<div class="board">

  <!-- Page 1: cover -->
  <section class="page p1">
    <div class="a brand"><span class="brand-mark"></span><span class="brand-name">QUILLMARSH<br><span style="font-size:11px;letter-spacing:3px;font-weight:700">PARTNERS</span></span></div>
    <svg class="a hero-svg" width="634" height="356" viewBox="0 0 634 356">
      <defs>
        <linearGradient id="cityTone" x1="0" y1="0" x2="0" y2="1">
          <stop offset="0" stop-color="#5b7fb1"/>
          <stop offset=".45" stop-color="#c9b8a6"/>
          <stop offset="1" stop-color="#7d7f86"/>
        </linearGradient>
      </defs>
      <polygon points="0,182 282,182 352,356 0,356" fill="#1f8bd0"/>
      <polygon points="342,0 532,0 634,205 545,356 372,356 290,182 440,182" fill="url(#cityTone)" role="img" aria-label="City skyline photograph under a bright morning sky"/>
      <polygon points="528,0 560,0 634,140 634,205" fill="#f7941d"/>
      <polygon points="568,0 634,0 634,120" fill="#f15a24"/>
      <polygon points="634,225 634,356 546,356" fill="#c3e5f8"/>
    </svg>
    <h1 class="a hero-title">HarborLeap provides executives and business owners with clear guidance to unlock non-financial value ahead of an exit.</h1>

    <div class="a lead-bar"></div>
    <div class="a lead body">
      <p>A strong communication and marketing strategy can significantly increase the value of your business leading up to an exit. Buyers are looking to mitigate risk and unlock potential value as a catalyst for clear growth potential.</p>
      <p>Highlighting your company’s success in the marketplace, identifying, and mitigating reptation risks before buyers do, enhancing employee engagement, finding hidden opportunities to boost marketing KPIs and showcasing IP, data, and innovation, can make a significant difference in valuation.</p>
    </div>

    <svg class="a callout" width="634" height="130" viewBox="0 0 634 130">
      <polygon points="46,5 562,5 588,105 505,105 476,128 447,105 72,105" fill="#c3e5f8"/>
    </svg>
    <div class="a callout-text">
      <em>US institutional investors believe that Investor Relations (IR) accounts for a total variance of 30% in a company’s valuation – from a premium of 10% for “superb” IR to a discount of 20% for “poor” IR.</em>
      Corvant Research Group, “Harnessing IR’s Power to Impact a Company’s Valuation.”
    </div>

    <p class="a support">We design and implement communication and marketing strategies that deliver significant increases in brand awareness, identify reputational risks, and enhance brand perception, helping owners and investors to realize premium values for their companies. We support owners and companies through:</p>
    <ul class="a list stages">
      <li><span class="tick"></span>Company Exit</li>
      <li><span class="tick"></span>Preparation</li>
      <li><span class="tick"></span>M&amp;A</li>
      <li><span class="tick"></span>IPO</li>
      <li><span class="tick"></span>Spinoff/Divestiture</li>
      <li><span class="tick"></span>New Leadership/Investor</li>
    </ul>

    <div class="a band-foot">Few sellers would list their home without first inspecting, repairing broken items, and making updates to highlight the positive aspects --increasing appeal to buyers. However, countless business owners leave money on the table during corporate exits due to a lack of preparation.</div>
  </section>

  <!-- Page 2: valuation -->
  <section class="page p2">
    <p class="a team body">Our team of executive-level communications and marketing experts brings deep buy and sell-side experience. We have played critical roles in the acquisition, integration, and disposition process. Our mix of financial services expertise combined with decades of experience leading internal and external ommunications, marketing and investor relations teams gives us a unique perspective on identifying and unlocking non-financial areas of value and mitigating non-financial risks before exit.</p>
    <div class="a band-blue">While accounting and investment banking teams are hard at work increasing value from a financial perspective, we help organizations enhance their valuation by identifying areas that will appeal most to buyers and ensuring those elements of your business are visible and memorable to those who matter most.</div>
    <h2 class="a help-title orange-b">We help companies increase valuation by:</h2>
    <div class="a pillar" style="left:54px"><div class="ring"></div><p>Highlighting value in a clear and visible way</p></div>
    <div class="a pillar" style="left:197px"><div class="ring"></div><p>Streamlining the exit process</p></div>
    <div class="a pillar" style="left:325px"><div class="ring"></div><p>Identifying potential risks and suggesting mitigation measures</p></div>
    <div class="a pillar" style="left:460px"><div class="ring"></div><p>Creating a polished presence in the market ahead of buyer interest</p></div>
    <div class="a rule"></div>
    <p class="a intro2 body">HarborLeap provides executives and business owners with clear guidance to unlock value ahead of an exit. Our non-disruptive, ala-carte process enables us to work with sellers on specific areas or to do a complete analysis and recommendation and can include:</p>
    <h3 class="a orange-b sec-title" style="left:53px;top:540px">Brand Analysis and Recommendations</h3>
    <p class="a blue-b" style="left:53px;top:570px;width:520px;font-size:12px;line-height:14px">Strong brands command a higher valuation. We conduct a brand analysis, providing clear and detailed recommendations to enhance your value proposition and help you stand out from the crowd:</p>
    <ul class="a list brand-items body">
      <li><span class="tick"></span><span class="orange-b">Current external position among competitors</span>We look at how your brand measures up based on external competitive analysis, positioning in the media and analyst community, and across other digital channels.</li>
      <li><span class="tick"></span><span class="orange-b">Physical brand image</span>A little bit of paint and updated fixtures can go a long way when increasing the value of a home. The same is true for businesses. Our audit evaluates non-disruptive steps your company can take to enhance your brand look and feel before sale.</li>
      <li><span class="tick"></span><span class="orange-b">Employee brand perception</span>We conduct a high-level external audit with recommendations to enhance engagement for current and prospective employees.</li>
      <li><span class="tick"></span><span class="orange-b">Customer brand perception</span>We conduct a high-level external audit showcasing how customers perceive your brand In the market. We then provide recommendations for enhancing engagement and maximizing value.</li>
    </ul>
    <div class="strip"></div>
  </section>

  <!-- Page 3: marketing -->
  <section class="page p3">
    <div class="a stat-box" style="top:38px;background:var(--blue)">A 5% increase in customer retention correlates with at least a 25% increase in profit, according to an analysis by Halden &amp; Company.<span class="stat-notch" style="border-top:22px solid var(--blue)"></span></div>
    <div class="a stat-box" style="top:181px;background:var(--orange)">It costs 5 times more to acquire a new customer than to retain a current one and 16 times more to get new customers to the same spending level as existing ones.<span class="stat-notch" style="border-top:22px solid var(--orange)"></span></div>

    <h2 class="a blue-b mk-title">Digital and Traditional Marketing Analysis and Recommendations</h2>
    <p class="a mk-left">How much money are you leaving on the table? Our marketing audits help organizations identify areas of hidden value that can have significant impacts on revenue and valuation. We optimize current activities and uncover new strategies to increase the effectiveness of current marketing spend. Areas we evaluate include:</p>
    <ul class="a list mk-list blue-b">
      <li><span class="tick"></span>Website traffic and conversion</li>
      <li><span class="tick"></span>CRM process review to identify strategies and recommendations to increase conversion and reactive old-leads</li>
      <li><span class="tick"></span>Email marketing strategy</li>
      <li><span class="tick"></span>Automations and drip marketing</li>
      <li><span class="tick"></span>Social media strategy /presence</li>
      <li><span class="tick"></span>Partnership marketing</li>
      <li><span class="tick"></span>Paid media analysis/strategy</li>
      <li><span class="tick"></span>suggestion</li>
    </ul>
    <div class="a mk-right">
      <h3 class="orange-b">Messaging and Content Strategy<br>Review and Analysis</h3>
      <p class="body">It’s about your valuation. Full and fair valuation requires a clear, compelling investment case articulated consistently to the right audience at the right time. Messaging to maximize your value in an acquisition or an IPO is quite different from typical selling messages for prospects, customers, or ‘features &amp; business benefits’ for press and analysts. We understand the issues and speak the right language to maximize perception of value with key decision makers.</p>
    </div>
    <ul class="a list msg-list blue-b">
      <li><span class="tick"></span>Review and recommendations of key messaging and value proposition</li>
      <li><span class="tick"></span>Analysis and recommendations to highlight data, IP, and innovation</li>
      <li><span class="tick"></span>Analysis and recommendations to position key executives likely to remain with the company as thought leaders to help build value</li>
      <li><span class="tick"></span>Analysis and recommendations to build employee engagement and retention enhancing your most valuable asset your team</li>
    </ul>
    <div class="strip"></div>
  </section>

  <!-- Page 4: media & deliverables -->
  <section class="page p4">
    <h2 class="a orange-b media-title">Media and Analyst Strategy Development</h2>
    <p class="a media-body body">Positive articles and inclusion in analyst reports pack a powerful punch when preparing your business for sale. We work with clients to develop a media strategy that goes beyond brand awareness, leveraging media to build a digital history of third-party validation targeted to enhance appeal to prospective buyers while generating traffic and connections, to enhance overall value.</p>
    <ul class="a list media-list blue-b">
      <li><span class="tick"></span>Positioning to media and analyst community creating third party market validation</li>
      <li><span class="tick"></span>Key angle recommendations</li>
      <li><span class="tick"></span>Announcement timeline and strategy planning to maximize media value of news What is newsworthy</li>
      <li><span class="tick"></span>How to position that news for the most significant impact</li>
    </ul>
    <div class="a sky-band"></div>
    <div class="a deep-band"></div>
    <div class="a orange-strip"></div>
    <h3 class="a blue-b wh-title">“White Hat/Black Hat Review”</h3>
    <p class="a wh-body">We take a buyer’s communications and marketing approach to analyzing the client company and provide a “punch list” of things a potential buyer is likely to ask/request in due diligence from a comms/culture/marketing/reputation standpoint to ensure that when potential buyers start screening for sellers and evaluating them, the client company has the upper hand.</p>
    <svg class="a" style="left:0;top:440px" width="634" height="130" viewBox="0 0 634 130">
      <polygon points="62,3 565,3 588,103 505,103 475,126 446,103 45,103" fill="#f7941d"/>
    </svg>
    <p class="a quote-text">“Strategy without tactics is the slowest route to victory. Tactics without strategy is the noise before defeat.” – Iven Torass</p>
    <p class="a after">Once the analysis is complete, we deliver actionable intelligence and recommendations to help leaders identify and quickly unlock areas that will boost value and appeal to prospective buyers. Work products include:</p>
    <div class="a product" style="top:641px">
      <h4><span class="tick light"></span>Gap Assessment</h4>
      <p>We provide a comprehensive seller report providing analysis and actionable recommendations to increase your valuation while identifying and mitigating non-financial risks.</p>
    </div>
    <div class="a product" style="top:745px">
      <h4 style="font-size:12.5px"><span class="tick light"></span>Strategic Roadmap</h4>
      <p style="margin-top:14px">Clients are given an actionable tactical roadmap based on the recommendation provided. Organizations can choose to implement key areas or include this powerful guide as part of their presentation to prospective buyers to highlight latent potential. The roadmap provides actionable steps buyers can take upon close as they make their case for your business with their investment committees.</p>
    </div>
  </section>

</div>
</body>
</html>
```